Business Cards for a law firm

Business cards for our law firm. Use our silhoette logo and OAK HARBOR - check our website (www.oakharbor-legal.com)

Contact Information for Business Card

our silhouette logo, OAK HARBOR, 800-555-0147, Dorian Kestrup, dorian@oakharbor-legal.com

Requirements
Must have
• our silhouette logo, OAK HARBOR, 800-555-0147, Dorian Kestrup, dorian@oakharbor-legal.com

```html
<!DOCTYPE html>
<html lang="en">
<head>
<meta charset="utf-8">
<title>Oak Harbor — Business Cards</title>
<link rel="stylesheet" href="https://fonts.googleapis.com/css2?family=Montserrat:wght@400;800&family=PT+Serif&display=swap">
<style>
  :root {
    --bg: #2a2a2b;
    --card: #ffffff;
    --card-shade: #ececec;
    --navy: #1f2d6b;
    --ink: #4a4a4a;
    --rule: #b9b9b9;
  }
  * { margin: 0; padding: 0; box-sizing: border-box; }
  html, body { width: 1200px; height: 900px; overflow: hidden; }
  body {
    background: var(--bg);
    display: flex;
    flex-direction: column;
    align-items: center;
    justify-content: center;
    gap: 50px;
  }
  .card {
    width: 700px;
    height: 400px;
    border-radius: 40px;
    background: linear-gradient(120deg, var(--card) 40%, var(--card-shade) 100%);
    position: relative;
    overflow: hidden;
  }
  .card-front {
    display: flex;
    align-items: center;
    justify-content: center;
    gap: 22px;
  }
  .brand-square {
    width: 48px;
    height: 48px;
    background: var(--navy);
  }
  .brand-name {
    font-family: "Montserrat", sans-serif;
    font-weight: 400;
    font-size: 50px;
    letter-spacing: 2px;
    color: var(--navy);
  }
  .card-back {
    display: flex;
    align-items: center;
  }
  .mark-area {
    width: 250px;
    height: 260px;
    margin-left: 70px;
    background: linear-gradient(180deg, #dfe2ee, #c9cee3);
    border-radius: 6px;
  }
  .divider {
    width: 1px;
    height: 240px;
    background: var(--rule);
    margin: 0 40px 0 45px;
  }
  .details { display: flex; flex-direction: column; gap: 10px; }
  .person-name {
    font-family: "Montserrat", sans-serif;
    font-weight: 800;
    font-size: 26px;
    letter-spacing: 1px;
    color: var(--navy);
    margin-bottom: 8px;
  }
  .contact-line {
    display: flex;
    align-items: center;
    gap: 10px;
    font-family: "PT Serif", serif;
    font-size: 19px;
    color: var(--ink);
  }
  .contact-line svg { width: 18px; height: 18px; flex: none; }
</style>
</head>
<body>
  <section class="card card-front">
    <div class="brand-square"></div>
    <div class="brand-name">OAK HARBOR</div>
  </section>

  <section class="card card-back">
    <div class="mark-area" role="img" aria-label="Firm silhouette mark area"></div>
    <div class="divider"></div>
    <div class="details">
      <div class="person-name">DORIAN KESTRUP</div>
      <div class="contact-line">
        <svg viewBox="0 0 24 24" aria-hidden="true"><path fill="#1f2d6b" d="M6.6 10.8a15 15 0 0 0 6.6 6.6l2.2-2.2a1 1 0 0 1 1-.25 11.4 11.4 0 0 0 3.6.6 1 1 0 0 1 1 1V20a1 1 0 0 1-1 1A17 17 0 0 1 3 4a1 1 0 0 1 1-1h3.5a1 1 0 0 1 1 1c0 1.25.2 2.45.6 3.6a1 1 0 0 1-.25 1z"/></svg>
        <span>800-555-0147</span>
      </div>
      <div class="contact-line">
        <svg viewBox="0 0 24 24" aria-hidden="true"><rect x="2" y="5" width="20" height="14" fill="#1f2d6b"/><path d="M2 5l10 8 10-8" fill="none" stroke="#fff" stroke-width="1.6"/></svg>
        <span>dorian@oakharbor-legal.com</span>
      </div>
      <div class="contact-line">
        <svg viewBox="0 0 24 24" aria-hidden="true"><g fill="none" stroke="#1f2d6b" stroke-width="1.6"><circle cx="12" cy="12" r="9.5"/><ellipse cx="12" cy="12" rx="4" ry="9.5"/><path d="M2.5 12h19M4 7h16M4 17h16"/></g></svg>
        <span>www.oakharbor-legal.com</span>
      </div>
    </div>
  </section>
</body>
</html>
```